Landing Page & Email Signature

I am looking for a new landing page as well as an email signature to align with the change in business. I have included the new logo/emblem which I'd like incorporated into the design and the current landing page is www.kelbrowinto.com.au should you wish to see the old version.

```html
<!DOCTYPE html>
<html lang="en">
<head>
<meta charset="utf-8">
<title>Kelbrow Transport – Quote Template</title>
<link href="https://fonts.googleapis.com/css2?family=Audiowide&family=Lato:wght@400;700&display=swap" rel="stylesheet">
<style>
:root{
  --ink:#141416;
  --red:#b5121b;
  --text:#2a2a2a;
  --line:#b9b9b9;
  --white:#ffffff;
  --muted:#d8d8d8;
}
*{box-sizing:border-box;margin:0;padding:0}
html,body{width:766px;height:1200px;overflow:hidden;background:var(--white)}
body{position:relative;font-family:'Lato',sans-serif;color:var(--text)}
.abs{position:absolute}
.display{font-family:'Audiowide',sans-serif;letter-spacing:1px}

/* top bar */
.topbar{left:0;top:0;width:766px;height:42px;background:var(--ink)}
.social{display:flex;gap:14px;align-items:center}
.social span{width:13px;height:13px;border-radius:50%;background:#cfcfcf;display:block}
.topbar .social{left:48px;top:15px}
.contact{top:13px;color:var(--white);font-size:12px;display:flex;align-items:center;gap:8px}
.contact.phone{left:395px;font-weight:700}
.contact.mail{left:522px}

/* header */
.brand{left:48px;top:62px}
.brand-name{font-size:19px;font-weight:700;color:var(--ink);letter-spacing:1px;line-height:1.1}
.brand-url{font-size:8px;font-weight:700;color:var(--red);margin-top:6px;display:flex;align-items:center;gap:5px}
.brand-url i{width:8px;height:8px;background:var(--red);border-radius:50%;display:block}
.nav{top:83px;left:276px;display:flex;gap:30px;font-size:10px;font-weight:700;color:var(--ink)}
.nav .active{color:var(--red)}

/* hero */
.hero{left:0;top:130px;width:766px;height:197px;
  background:linear-gradient(100deg,#2c4f86 0%,#b8503e 30%,#2d5a9a 50%,#c9432e 62%,#6f94c4 78%,#2f5f9d 100%)}
.hero::after{content:"";position:absolute;inset:0;background:rgba(20,25,40,.35)}
.hero-title{left:0;top:212px;width:766px;text-align:center;color:var(--white);font-size:27px;z-index:1}

/* form */
.page-title{left:0;top:364px;width:766px;text-align:center;font-size:20px;color:var(--ink)}
.page-sub{left:0;top:404px;width:766px;text-align:center;font-size:11px}
.group-title{left:48px;font-size:14px;color:var(--red)}
.field{width:155px;height:34px;border:1px solid var(--line);font-size:11px;padding:0 10px;display:flex;align-items:center}
.q{left:47px;width:680px;font-size:11px;line-height:18.5px}
.radios{left:48px;display:flex;gap:17px;font-size:11px;align-items:center}
.radios label{display:flex;align-items:center;gap:5px}
.radios i{width:11px;height:11px;border:1px solid #999;border-radius:50%;display:block}
.btn{left:48px;top:902px;width:131px;height:32px;background:var(--red);color:var(--white);font-size:9.5px;display:flex;align-items:center;justify-content:center}

/* footer */
.footer{left:0;top:987px;width:766px;height:213px;background:var(--ink);color:var(--white)}
.footer .brand-name{color:var(--white);font-size:19px}
.footer .brand-url{color:var(--white)}
.footer .brand-url i{background:var(--white)}
.f-about{left:48px;top:120px;width:215px;font-size:10px;line-height:17px}
.f-head{font-size:11.5px;top:38px}
.f-list{font-size:9.5px;list-style:none}
.f-list.nav-links li{height:20.8px}
.f-list.quick li{height:17.8px}
.footer .social{left:578px;top:72px;gap:17px}
.footer .social span{width:14px;height:14px;background:#bdbdbd}
.copy{left:578px;top:110px;font-size:8.5px;line-height:14px}
</style>
</head>
<body>

<div class="abs topbar">
  <div class="abs social"><span></span><span></span><span></span><span></span><span></span></div>
  <div class="abs contact phone">
    <svg width="10" height="11" viewBox="0 0 10 11"><path d="M2 1l2 2-1 1.5c.6 1.4 1.6 2.4 3 3L7.5 6l2 2-1.3 1.5C4.5 9.5 .5 5.5.5 2.3z" fill="#fff"/></svg>
    +61400123456
  </div>
  <div class="abs contact mail">
    <svg width="12" height="9" viewBox="0 0 12 9"><rect width="12" height="9" rx="1" fill="#fff"/><path d="M0 1l6 4 6-4" stroke="#141416" fill="none"/></svg>
    kelbrowlogistics@mail.com
  </div>
</div>

<div class="abs brand">
  <div class="brand-name">KELBROW<br>TRANSPORT</div>
  <div class="brand-url"><i></i>www.kelbrowinto.com.au</div>
</div>
<nav class="abs nav">
  <span class="active">HOME</span><span>ABOUT US</span><span>SERVICES</span><span>LATEST NEWS</span><span>REVIEWS</span><span>CONTACT US</span>
</nav>

<div class="abs hero" role="img" aria-label="Stacked shipping containers with a container handler lifting a red container"></div>
<h1 class="abs hero-title display">QUOTE TEMPLATE</h1>

<h2 class="abs page-title display">QUOTE TEMPLATE</h2>
<p class="abs page-sub">Services Please fill in the the form below to get a quote.</p>

<h3 class="abs group-title display" style="top:444px">YOUR DETAILS</h3>
<div class="abs field" style="left:48px;top:475px">First Name*</div>
<div class="abs field" style="left:221px;top:475px">Last Name*</div>
<div class="abs field" style="left:393px;top:475px">Company Email*</div>
<div class="abs field" style="left:566px;top:475px">Phone Mobile*</div>

<h3 class="abs group-title display" style="top:532px">MOTORCYCLE DETAILS</h3>
<div class="abs field" style="left:48px;top:562px">Motorcycle Make*</div>
<div class="abs field" style="left:221px;top:562px">Model*</div>
<div class="abs field" style="left:393px;top:562px">Colour*</div>
<div class="abs field" style="left:566px;top:562px">Rego / VIN*</div>

<p class="abs q" style="top:614px">Panniers Top BoxApe HangersWindscreenTank Bag Is the bike rollable?</p>
<div class="abs radios" style="top:650px"><label><i></i>Yes</label><label><i></i>No</label></div>

<p class="abs q" style="top:676px;width:690px">Additional Information Motorcyle #2 Details Motorcycle Make Model Type 2 WheelerTrikeQuadExtra LengthMini BikeOther Accessories PanniersTop BoxApe HangersWindscreenTank Bag Is the bike rollable?</p>
<div class="abs radios" style="top:722px"><label><i></i>Yes</label><label><i></i>No</label></div>

<p class="abs q" style="top:746px;left:50px">Additional Information Pickup Details Pickup Suburb/Town Pickup State Pickup Postcode Is this bike from an AUCTION?</p>
<div class="abs radios" style="top:775px"><label><i></i>Yes</label><label><i></i>No</label></div>

<p class="abs q" style="top:803px">Delivery Details Delivery Suburb/Town Delivery State Delivery Postcode Click here for additional fees &amp; regulations on sending extra items such as helmets, exhausts, parts etc.</p>
<div class="abs radios" style="top:848px"><label><i></i>Yes</label><label><i></i>No</label></div>

<div class="abs btn display">QUOTED PRICE</div>

<footer class="abs footer">
  <div class="abs brand" style="top:40px">
    <div class="brand-name">KELBROW<br>TRANSPORT</div>
    <div class="brand-url"><i></i>www.kelbrowinto.com.au</div>
  </div>
  <p class="abs f-about">Duis aute irure dolor in reprehenderit in voluptate velit esse cillum dolore eu fugiat nulla pariatur occaecat cupidatat non .</p>

  <h4 class="abs f-head display" style="left:280px">NAVIGATION</h4>
  <ul class="abs f-list nav-links" style="left:280px;top:60px">
    <li>Home</li><li>About Us</li><li>Services</li><li>Latest New</li><li>Reviews</li><li>Contact Us</li>
  </ul>

  <h4 class="abs f-head display" style="left:429px">QUICK LINKS</h4>
  <ul class="abs f-list quick" style="left:429px;top:57px">
    <li>Duis aute irure</li><li>Reprehend</li><li>Voluptate velit esse</li><li>Cillum dolore</li><li>Pariatur</li>
  </ul>

  <h4 class="abs f-head display" style="left:578px">FOLLOW US</h4>
  <div class="abs social"><span></span><span></span><span></span><span></span><span></span></div>
  <p class="abs copy">Copyright © 2022. Company Name<br>All Right Reserved</p>
</footer>

</body>
</html>
```